Präsentationsvorlagen für Vorträge
Zielgruppe
Wir machen laborbasierte Selbsttests im Bereich Longevity und bieten dazu auch passende Supplements an
Aufgabenstellung
Ich brauche eine Präsentationsvorlage für Vorträge basierend auf den Farben und Logo in den angehängten Dateien. Soll alles was für Präsentation nötig ist berücksichtigen

```html
<!DOCTYPE html>
<html lang="en">
<head>
<meta charset="utf-8">
<title>Brunnfeld – Presentation Template</title>
<link href="https://fonts.googleapis.com/css2?family=Montserrat:ital,wght@0,400;0,500;0,600;0,700;1,400&display=swap" rel="stylesheet">
<style>
:root{
  --teal:#0d4f4a;
  --green:#8cc63f;
  --green-line:#d4e8b6;
  --ink:#1f2d2b;
  --gray:#6b7573;
  --faint:#b5bcba;
  --stage:#e6e6e6;
  --white:#ffffff;
}
html,body{margin:0;padding:0;overflow:hidden}
body{font-family:"Montserrat",sans-serif;color:var(--ink)}
.canvas{position:relative;width:1200px;height:3027px;background:var(--stage);overflow:hidden}

.slide{position:absolute;width:474px;height:266px;background:var(--white);overflow:hidden}
.slide--dark{background:var(--teal)}
.hero-slide{transform-origin:0 0;transform:scale(.8);box-shadow:0 14px 30px rgba(0,0,0,.18)}

.abs{position:absolute}
.title{position:absolute;font:700 16px/1.2 "Montserrat",sans-serif;color:var(--teal);margin:0}
.title--light{color:var(--white)}
.pill{background:var(--green);color:var(--white);border-radius:8px;padding:0 4px}
.body{font-size:5.3px;line-height:1.6;color:var(--gray);margin:0}
.body--light{color:#d6e4e2}
.strong{font-weight:700;color:var(--ink)}
.sub{font-weight:700;font-size:6.5px;color:var(--ink);margin:0}
.kicker{font-weight:600;font-size:7px;color:var(--green);margin:0}

.brand-sm{position:absolute;right:18px;top:15px;display:flex;align-items:center;gap:3px;font:700 9px "Montserrat",sans-serif;color:var(--teal)}
.brand-sm::before{content:"";width:6px;height:6px;border-radius:50%;background:var(--green)}
.brand-lg{position:absolute;left:36px;top:32px;font:700 19px "Montserrat",sans-serif;color:var(--white);display:flex;align-items:center;gap:6px}
.brand-lg::before{content:"";width:13px;height:13px;border-radius:50%;background:var(--green)}
.brand-lg--dark{color:var(--teal)}
.tagline{position:absolute;left:55px;top:56px;font-size:6.5px;color:var(--green);font-weight:500}

.foot{position:absolute;left:16px;bottom:12px;font-size:3.6px;color:var(--faint)}
.pg{position:absolute;right:16px;bottom:10px;width:8px;height:10px;border:1px solid var(--green);border-radius:2px;font-size:4.5px;text-align:center;line-height:10px;color:var(--teal)}

.cover-big{position:absolute;left:36px;top:103px;margin:0;line-height:1}
.cover-big .w1{display:block;font-size:28px;font-weight:400;letter-spacing:.5px}
.cover-big .w2{display:block;font-size:28px;font-weight:700;color:var(--green);margin-top:2px}
.cover-big .w3{display:block;font-size:13px;font-weight:400;margin-top:6px}
.url{position:absolute;left:28px;top:234px;font-size:7px;padding:2px 10px;border:1px solid var(--green);border-radius:8px}
.photo{position:absolute}

.toc-row{position:absolute;left:250px;width:170px;height:26px;border-bottom:1px solid var(--green-line);display:flex;justify-content:space-between;align-items:flex-end;padding-bottom:3px;box-sizing:border-box}
.toc-row span:first-child{font-size:7px;font-weight:600;color:var(--teal)}
.toc-row span:last-child{font-size:15px;font-weight:400;color:var(--green);line-height:1}

.card{position:absolute;width:120px;height:62px;border:1px solid var(--green-line);border-radius:5px;box-sizing:border-box;padding:9px 8px 0 18px}
.tick{position:absolute;left:-5px;top:-5px;width:16px;height:16px;border-radius:50%;background:var(--green)}
.tick svg{display:block}
.bullets{margin:0;padding:0 0 0 8px;list-style:none}
.bullets li{position:relative;font-size:5.3px;line-height:1.6;color:var(--gray);margin-bottom:6px}
.bullets li::before{content:"";position:absolute;left:-7px;top:2px;width:3px;height:3px;border-radius:50%;background:var(--green)}

.quote-box{position:absolute;background:var(--white);border-radius:5px;box-shadow:0 4px 14px rgba(0,0,0,.08);padding:12px;box-sizing:border-box}
.feature{position:absolute;display:flex;gap:6px;width:110px}
.feature .ico{flex:0 0 14px;height:14px;border:1px solid var(--green);border-radius:50%}
.num{font-size:14px;color:var(--green);font-weight:400;line-height:1}
.value{position:absolute;display:flex;gap:6px;align-items:flex-start}
.value .sub{color:var(--teal)}
.bracket{position:absolute;border:4px solid var(--green);border-radius:10px}
.badge{position:absolute;background:var(--green);color:#fff;border-radius:4px;padding:3px 10px;font-size:6px;font-weight:700;text-align:center;line-height:1.3}
</style>
</head>
<body>
<div class="canvas">

  <!-- Hero group -->
  <section class="slide hero-slide" style="left:275px;top:95px" aria-label="About us slide">
    <h2 class="title" style="left:45px;top:40px">About <span class="pill">us</span></h2>
    <p class="kicker abs" style="left:45px;top:66px">Welcome to Brunnfeld</p>
    <p class="body abs" style="left:45px;top:80px;width:180px">Lorem ipsum dolor sit amet, consectetuer adipiscing elit, sed diam nonummy nibh euismod tincidunt ut laoreet dolore magna aliquam erat volutpat. Ut wisi enim ad minim veniam, quis nostrud exerci tation ullamcorper suscipit lobortis nisl ut aliquip ex ea commodo consequat.</p>
    <div class="abs" style="left:45px;top:150px;width:2px;height:26px;background:var(--green)"></div>
    <p class="body abs" style="left:55px;top:150px;width:170px;font-style:italic">Lorem ipsum dolor sit amet, consectetuer adipiscing elit, sed diam nonummy nibh euismod tincidunt ut laoreet dolore magna aliquam.</p>
    <div class="brand-sm">Brunnfeld</div>
    <div class="photo" role="img" aria-label="Portrait photo of a smiling doctor in a white coat" style="left:300px;top:40px;width:150px;height:226px;background:linear-gradient(180deg,#eef1f0,#c9d3d1)"></div>
    <div class="badge" style="left:322px;top:212px">Dr. Jonas Beispiel<br><span style="font-weight:400">Geschäftsführer</span></div>
  </section>

  <section class="slide slide--dark hero-slide" style="left:600px;top:205px" aria-label="Cover slide">
    <div class="photo" role="img" aria-label="Photo of an older couple jogging in a park" style="left:200px;top:0;width:274px;height:266px;background:linear-gradient(90deg,var(--teal),#4d7e6a 55%,#7b9a83)"></div>
    <div class="brand-lg">Brunnfeld</div>
    <div class="tagline">Stark durch jeden Tag</div>
    <h1 class="cover-big" style="color:#fff"><span class="w1">COMPANY</span><span class="w2">PRESENTATION</span><span class="w3">Your subtitle texts goes here</span></h1>
    <div class="url" style="color:#fff">www.brunnfeld-beispiel.de</div>
  </section>

  <section class="slide hero-slide" style="left:170px;top:345px" aria-label="Table of content slide">
    <h2 class="title" style="left:45px;top:55px">Table <span class="pill">of</span><br>Content</h2>
    <div class="toc-row" style="top:60px"><span>Introduction</span><span>03</span></div>
    <div class="toc-row" style="top:92px"><span>Improving our Health</span><span>05</span></div>
    <div class="toc-row" style="top:124px"><span>Why you should choose us</span><span>06</span></div>
    <div class="toc-row" style="top:156px"><span>Our Product</span><span>07</span></div>
    <div class="toc-row" style="top:188px"><span>Market Research</span><span>08</span></div>
    <p class="body strong abs" style="left:45px;top:185px;width:170px">Lorem ipsum dolor sit amet, consectetuer adipiscing elit, sed diam nonummy nibh euismod tincidunt ut laoreet dolore magna aliquam erat volutpat.</p>
    <div class="brand-sm">Brunnfeld</div>
    <div class="pg">2</div>
  </section>

  <section class="slide hero-slide" style="left:595px;top:445px" aria-label="Text and image slide">
    <div class="abs" style="left:0;top:0;width:290px;height:266px;background:var(--teal)"></div>
    <h2 class="title title--light" style="left:45px;top:20px">Lorem <span class="pill">ipsum</span><br>dolor sit amet</h2>
    <p class="body body--light abs" style="left:45px;top:100px;width:160px">Lorem ipsum dolor sit amet, consectetuer adipiscing elit, sed diam nonummy nibh euismod tincidunt ut laoreet dolore magna aliquam erat volutpat. Ut wisi enim ad minim veniam, quis nostrud exerci tation ullamcorper suscipit lobortis nisl ut aliquip ex ea commodo consequat.</p>
    <div class="brand-sm">Brunnfeld</div>
    <div class="bracket" style="left:225px;top:88px;width:225px;height:150px;border-top:none;border-left:none"></div>
    <div class="photo" role="img" aria-label="Photo of a doctor consulting an older patient" style="left:232px;top:80px;width:220px;height:150px;border-radius:8px;background:linear-gradient(135deg,#e9ecea,#c4ccc8)"></div>
    <div class="pg">4</div>
  </section>

  <!-- Row 1 -->
  <section class="slide slide--dark" style="left:122px;top:870px" aria-label="Cover slide dark">
    <div class="photo" role="img" aria-label="Photo of an older couple jogging in a park" style="left:200px;top:0;width:274px;height:266px;background:linear-gradient(90deg,var(--teal),#4d7e6a 55%,#7b9a83)"></div>
    <div class="brand-lg">Brunnfeld</div>
    <div class="tagline">Stark durch jeden Tag</div>
    <h1 class="cover-big" style="color:#fff"><span class="w1">COMPANY</span><span class="w2">PRESENTATION</span><span class="w3">Your subtitle texts goes here</span></h1>
    <div class="url" style="color:#fff">www.brunnfeld-beispiel.de</div>
  </section>

  <section class="slide" style="left:621px;top:870px" aria-label="Cover slide light">
    <div class="photo" role="img" aria-label="Photo of an older couple jogging in a park" style="left:200px;top:0;width:274px;height:266px;background:linear-gradient(90deg,#ffffff,#c8d4c6 55%,#8fa892)"></div>
    <div class="brand-lg brand-lg--dark">Brunnfeld</div>
    <div class="tagline">Stark durch jeden Tag</div>
    <h1 class="cover-big" style="color:var(--teal)"><span class="w1">COMPANY</span><span class="w2">PRESENTATION</span><span class="w3">Your subtitle texts goes here</span></h1>
    <div class="url" style="color:var(--teal)">www.brunnfeld-beispiel.de</div>
  </section>

  <!-- Row 2 -->
  <section class="slide" style="left:122px;top:1166px" aria-label="Table of content slide">
    <div class="brand-sm">Brunnfeld</div>
    <h2 class="title" style="left:45px;top:55px">Table <span class="pill">of</span><br>Content</h2>
    <div class="toc-row" style="top:60px"><span>Introduction</span><span>03</span></div>
    <div class="toc-row" style="top:92px"><span>Improving our Health</span><span>05</span></div>
    <div class="toc-row" style="top:124px"><span>Why you should choose us</span><span>06</span></div>
    <div class="toc-row" style="top:156px"><span>Our Product</span><span>07</span></div>
    <div class="toc-row" style="top:188px"><span>Market Research</span><span>08</span></div>
    <p class="body strong abs" style="left:45px;top:185px;width:170px">Lorem ipsum dolor sit amet, consectetuer adipiscing elit, sed diam nonummy nibh euismod tincidunt ut laoreet dolore magna aliquam erat volutpat. Ut wisi enim ad minim veniam, quis nostrud</p>
    <div class="foot">Your presentation title goes here | Brunnfeld GmbH 2023</div>
    <div class="pg">2</div>
  </section>

  <section class="slide" style="left:621px;top:1166px" aria-label="About us slide">
    <div class="brand-sm">Brunnfeld</div>
    <h2 class="title" style="left:45px;top:40px">About <span class="pill">us</span></h2>
    <p class="kicker abs" style="left:45px;top:66px">Welcome to Brunnfeld</p>
    <p class="body abs" style="left:45px;top:80px;width:180px">Lorem ipsum dolor sit amet, consectetuer adipiscing elit, sed diam nonummy nibh euismod tincidunt ut laoreet dolore magna aliquam erat volutpat. Ut wisi enim ad minim veniam, quis nostrud exerci tation ullamcorper suscipit lobortis nisl ut aliquip ex ea commodo consequat. Duis autem vel eum iriure dolor in hendrerit in vulputate velit esse molestie consequat, vel illum dolore eu feugiat nulla facilisis at vero eros et accumsan et iusto.</p>
    <div class="abs" style="left:45px;top:180px;width:2px;height:26px;background:var(--green)"></div>
    <p class="body abs" style="left:55px;top:180px;width:170px;font-style:italic">Lorem ipsum dolor sit amet, consectetuer adipiscing elit, sed diam nonummy nibh euismod tincidunt ut laoreet dolore magna aliquam erat volutpat.</p>
    <div class="photo" role="img" aria-label="Portrait photo of a smiling doctor in a white coat" style="left:300px;top:40px;width:150px;height:226px;background:linear-gradient(180deg,#eef1f0,#c9d3d1)"></div>
    <div class="badge" style="left:322px;top:212px">Dr. Jonas Beispiel<br><span style="font-weight:400">Geschäftsführer</span></div>
    <div class="foot">Your presentation title goes here | Brunnfeld GmbH 2023</div>
    <div class="pg">3</div>
  </section>

  <!-- Row 3 -->
  <section class="slide" style="left:122px;top:1462px" aria-label="Six point slide">
    <div class="brand-sm">Brunnfeld</div>
    <h2 class="title" style="left:32px;top:44px">Six <span class="pill">Point</span> Slide</h2>
    <div class="card" style="left:40px;top:82px"><span class="tick"><svg width="16" height="16" viewBox="0 0 16 16"><path d="M4.5 8.2l2.3 2.3 4.7-4.8" fill="none" stroke="#fff" stroke-width="1.6" stroke-linecap="round" stroke-linejoin="round"/></svg></span><p class="body"><span class="strong">Lorem ipsum dolor sit amet, consectetuer adipiscing elit</span><br>Lorem ipsum dolor sit amet, consectetuer adipiscing elit, sed diam nonummy nibh</p></div>
    <div class="card" style="left:178px;top:82px"><span class="tick"><svg width="16" height="16" viewBox="0 0 16 16"><path d="M4.5 8.2l2.3 2.3 4.7-4.8" fill="none" stroke="#fff" stroke-width="1.6" stroke-linecap="round" stroke-linejoin="round"/></svg></span><p class="body"><span class="strong">Lorem ipsum dolor sit amet, consectetuer adipiscing elit</span><br>Lorem ipsum dolor sit amet, consectetuer adipiscing elit, sed diam nonummy nibh</p></div>
    <div class="card" style="left:316px;top:82px"><span class="tick"><svg width="16" height="16" viewBox="0 0 16 16"><path d="M4.5 8.2l2.3 2.3 4.7-4.8" fill="none" stroke="#fff" stroke-width="1.6" stroke-linecap="round" stroke-linejoin="round"/></svg></span><p class="body"><span class="strong">Lorem ipsum dolor sit amet, consectetuer adipiscing elit</span><br>Lorem ipsum dolor sit amet, consectetuer adipiscing elit, sed diam nonummy nibh</p></div>
    <div class="card" style="left:40px;top:158px"><span class="tick"><svg width="16" height="16" viewBox="0 0 16 16"><path d="M4.5 8.2l2.3 2.3 4.7-4.8" fill="none" stroke="#fff" stroke-width="1.6" stroke-linecap="round" stroke-linejoin="round"/></svg></span><p class="body"><span class="strong">Lorem ipsum dolor sit amet, consectetuer adipiscing elit</span><br>Lorem ipsum dolor sit amet, consectetuer adipiscing elit, sed diam nonummy nibh</p></div>
    <div class="card" style="left:178px;top:158px"><span class="tick"><svg width="16" height="16" viewBox="0 0 16 16"><path d="M4.5 8.2l2.3 2.3 4.7-4.8" fill="none" stroke="#fff" stroke-width="1.6" stroke-linecap="round" stroke-linejoin="round"/></svg></span><p class="body"><span class="strong">Lorem ipsum dolor sit amet, consectetuer adipiscing elit</span><br>Lorem ipsum dolor sit amet, consectetuer adipiscing elit, sed diam nonummy nibh</p></div>
    <div class="card" style="left:316px;top:158px"><span class="tick"><svg width="16" height="16" viewBox="0 0 16 16"><path d="M4.5 8.2l2.3 2.3 4.7-4.8" fill="none" stroke="#fff" stroke-width="1.6" stroke-linecap="round" stroke-linejoin="round"/></svg></span><p class="body"><span class="strong">Lorem ipsum dolor sit amet, consectetuer adipiscing elit</span><br>Lorem ipsum dolor sit amet, consectetuer adipiscing elit, sed diam nonummy nibh</p></div>
    <div class="foot">Your presentation title goes here | Brunnfeld GmbH 2023</div>
    <div class="pg">3</div>
  </section>

  <section class="slide" style="left:621px;top:1462px" aria-label="Text slide with two columns">
    <div class="brand-sm">Brunnfeld</div>
    <h2 class="title" style="left:45px;top:36px">Text slide <span class="pill">with</span><br>two column</h2>
    <p class="sub abs" style="left:45px;top:96px">Our Vision</p>
    <p class="body abs" style="left:45px;top:108px;width:165px">Lorem ipsum dolor sit amet, consectetuer adipiscing elit, sed diam nonummy nibh euismod tincidunt ut laoreet dolore magna aliquam erat volutpat. Ut wisi enim ad minim veniam, quis nostrud exerci tation ullamcorper suscipit lobortis nisl ut aliquip ex ea commodo consequat. Duis autem vel eum iriure dolor in hendrerit in vulputate velit esse molestie consequat, vel illum dolore eu feugiat nulla facilisis at vero eros et accumsan et iusto.</p>
    <p class="sub abs" style="left:254px;top:96px">Our Mission</p>
    <ul class="bullets abs" style="left:254px;top:108px;width:170px">
      <li>Lorem ipsum dolor sit amet, consectetuer adipiscing elit, sed diam nonummy nibh euismod tincidunt.</li>
      <li>Lorem ipsum dolor sit amet, consectetuer adipiscing elit, sed diam nonummy nibh euismod tincidunt.</li>
      <li>Lorem ipsum dolor sit amet, consectetuer adipiscing elit, sed diam nonummy nibh euismod tincidunt.</li>
      <li>Lorem ipsum dolor sit amet, consectetuer adipiscing elit, sed diam nonummy nibh euismod tincidunt.</li>
    </ul>
    <div class="foot">Your presentation title goes here | Brunnfeld GmbH 2023</div>
    <div class="pg">4</div>
  </section>

  <!-- Row 4 -->
  <section class="slide" style="left:122px;top:1759px" aria-label="Text only slide">
    <div class="brand-sm">Brunnfeld</div>
    <h2 class="title" style="left:52px;top:44px">Text <span class="pill">only</span> slide</h2>
    <p class="body strong abs" style="left:52px;top:76px;width:370px;color:var(--teal)">Lorem ipsum dolor sit amet, consectetuer adipiscing elit, sed diam nonummy nibh euismod tincidunt ut laoreet dolore magna aliquam erat volutpat. Ut wisi enim ad minim veniam</p>
    <p class="body abs" style="left:52px;top:98px;width:370px">Lorem ipsum dolor sit amet, consectetuer adipiscing elit, sed diam nonummy nibh euismod tincidunt ut laoreet dolore magna aliquam erat volutpat. Ut wisi enim ad minim veniam, quis nostrud exerci tation ullamcorper suscipit lobortis nisl ut aliquip ex ea commodo consequat. Duis autem vel eum iriure dolor in hendrerit in vulputate velit esse molestie consequat, vel illum dolore eu feugiat nulla facilisis at vero eros et accumsan et iusto odio dignissim qui blandit praesent luptatum zzril delenit augue duis dolore te feugait nulla facilisi.</p>
    <div class="quote-box" style="left:62px;top:164px;width:170px;height:68px"><p class="sub" style="font-size:5.5px;color:var(--teal)">Lorem ipsum dolor sit amet</p><p class="body">Lorem ipsum dolor sit amet, consectetuer adipiscing elit, sed diam nonummy nibh euismod tincidunt ut laoreet dolore magna aliquam erat volutpat.</p></div>
    <div class="abs" style="left:260px;top:176px;width:150px"><p class="sub" style="font-size:5.5px;color:var(--teal)">Lorem ipsum dolor sit amet</p><p class="body">Lorem ipsum dolor sit amet, consectetuer adipiscing elit, sed diam nonummy nibh euismod tincidunt ut laoreet dolore magna aliquam erat volutpat.</p></div>
    <div class="foot">Your presentation title goes here | Brunnfeld GmbH 2023</div>
    <div class="pg">5</div>
  </section>

  <section class="slide" style="left:621px;top:1759px" aria-label="Text slide with three columns">
    <div class="brand-sm">Brunnfeld</div>
    <h2 class="title" style="left:45px;top:36px">Text slide <span class="pill">with</span><br>three column</h2>
    <p class="sub abs" style="left:45px;top:92px">Lorem Ipsum</p>
    <p class="body abs" style="left:45px;top:104px;width:122px">Lorem ipsum dolor sit amet, consectetuer adipiscing elit, sed diam nonummy nibh euismod tincidunt ut laoreet dolore magna aliquam erat volutpat. Ut wisi enim ad minim veniam, quis nostrud exerci tation ullamcorper suscipit lobortis nisl ut aliquip ex ea commodo consequat. Duis autem vel eum iriure dolor in hendrerit in vulputate velit esse molestie consequat, vel illum dolore eu feugiat nulla facilisis.</p>
    <p class="body abs" style="left:186px;top:104px;width:122px">Lorem ipsum dolor sit amet, consectetuer adipiscing elit, sed diam nonummy nibh euismod tincidunt ut laoreet dolore magna aliquam erat volutpat. Ut wisi enim ad minim veniam, quis nostrud exerci tation ullamcorper suscipit lobortis nisl ut aliquip ex ea commodo consequat. Duis autem vel eum iriure dolor in hendrerit in vulputate velit esse molestie consequat, vel illum dolore eu feugiat nulla facilisis.</p>
    <p class="body abs" style="left:327px;top:104px;width:122px">Lorem ipsum dolor sit amet, consectetuer adipiscing elit, sed diam nonummy nibh euismod tincidunt ut laoreet dolore magna aliquam erat volutpat. Ut wisi enim ad minim veniam, quis nostrud exerci tation ullamcorper suscipit lobortis nisl ut aliquip ex ea commodo consequat. Duis autem vel eum iriure dolor in hendrerit in vulputate velit esse molestie consequat, vel illum dolore eu feugiat nulla facilisis.</p>
    <div class="foot">Your presentation title goes here | Brunnfeld GmbH 2023</div>
    <div class="pg">5</div>
  </section>

  <!-- Row 5 -->
  <section class="slide" style="left:122px;top:2056px" aria-label="What we do slide">
    <div class="brand-sm">Brunnfeld</div>
    <h2 class="title" style="left:36px;top:54px">What <span class="pill">we</span> do?</h2>
    <p class="body abs" style="left:36px;top:80px;width:225px">Lorem ipsum dolor sit amet, consectetuer adipiscing elit, sed diam nonummy nibh euismod tincidunt ut laoreet dolore magna aliquam erat volutpat. Ut wisi enim ad minim veniam, quis nostrud exerci tation</p>
    <div class="feature" style="left:38px;top:124px"><span class="ico"></span><p class="body" style="color:var(--teal)">Lorem ipsum dolor sit amet, consectetuer adipiscing elit, sed diam nonummy nibh.</p></div>
    <div class="feature" style="left:158px;top:124px"><span class="ico"></span><p class="body" style="color:var(--teal)">Lorem ipsum dolor sit amet, consectetuer adipiscing elit, sed diam nonummy nibh.</p></div>
    <div class="feature" style="left:38px;top:166px"><span class="ico"></span><p class="body" style="color:var(--teal)">Lorem ipsum dolor sit amet, consectetuer adipiscing elit, sed diam nonummy nibh.</p></div>
    <div class="feature" style="left:158px;top:166px"><span class="ico"></span><p class="body" style="color:var(--teal)">Lorem ipsum dolor sit amet, consectetuer adipiscing elit, sed diam nonummy nibh.</p></div>
    <div class="bracket" style="left:300px;top:58px;width:150px;height:176px;border-left:none;border-bottom-color:transparent"></div>
    <div class="photo" role="img" aria-label="Photo of a laughing older couple outdoors" style="left:300px;top:64px;width:150px;height:170px;border-radius:12px;background:linear-gradient(135deg,#5b8fb8,#a9c3d3 60%,#d8d4c8)"></div>
    <div class="foot">Your presentation title goes here | Brunnfeld GmbH 2023</div>
    <div class="pg">6</div>
  </section>

  <section class="slide" style="left:621px;top:2056px" aria-label="Our value slide">
    <div class="brand-sm">Brunnfeld</div>
    <h2 class="title" style="left:52px;top:54px"><span class="pill">Our</span> Value</h2>
    <p class="body abs" style="left:186px;top:52px;width:245px">Lorem ipsum dolor sit amet, consectetuer adipiscing elit, sed diam nonummy nibh euismod tincidunt ut laoreet dolore magna aliquam erat volutpat. Ut wisi enim ad minim veniam, quis nostrud exerci tation</p>
    <div class="value" style="left:48px;top:112px"><span class="num">01</span><div><p class="sub">Lorem Ipsum</p><p class="body">Lorem ipsum dolor sit amet, consectetuer adipiscing</p></div></div>
    <div class="value" style="left:68px;top:152px"><span class="num">02</span><div><p class="sub">Lorem Ipsum</p><p class="body">Lorem ipsum dolor sit amet, consectetuer adipiscing</p></div></div>
    <div class="value" style="left:48px;top:192px"><span class="num">03</span><div><p class="sub">Lorem Ipsum</p><p class="body">Lorem ipsum dolor sit amet, consectetuer adipiscing</p></div></div>
    <div class="value" style="left:232px;top:112px"><span class="num">04</span><div><p class="sub">Lorem Ipsum</p><p class="body">Lorem ipsum dolor sit amet, consectetuer adipiscing</p></div></div>
    <div class="value" style="left:252px;top:152px"><span class="num">05</span><div><p class="sub">Lorem Ipsum</p><p class="body">Lorem ipsum dolor sit amet, consectetuer adipiscing</p></div></div>
    <div class="value" style="left:232px;top:192px"><span class="num">06</span><div><p class="sub">Lorem Ipsum</p><p class="body">Lorem ipsum dolor sit amet, consectetuer adipiscing</p></div></div>
    <div class="foot">Your presentation title goes here | Brunnfeld GmbH 2023</div>
    <div class="pg">6</div>
  </section>

  <!-- Row 6 -->
  <section class="slide" style="left:122px;top:2352px" aria-label="Section break slide">
    <div class="photo" role="img" aria-label="Photo of an older couple with their golden dog in a garden" style="left:0;top:0;width:474px;height:266px;background:linear-gradient(135deg,#3f6b3a,#8aa06a 45%,#d4b27a 70%,#6f8f5a)"></div>
    <div class="abs" style="left:20px;top:206px;width:434px;height:40px;border-radius:12px;background:var(--teal);display:flex;align-items:center;justify-content:space-between;padding:0 24px;box-sizing:border-box">
      <span style="display:flex;flex-direction:column">
        <span style="display:flex;align-items:center;gap:5px;font-weight:700;font-size:15px;color:#fff"><span style="width:10px;height:10px;border-radius:50%;background:var(--green)"></span>Brunnfeld</span>
        <span style="font-size:5.5px;color:var(--green);margin-left:15px">Stark durch jeden Tag</span>
      </span>
      <span style="font-size:20px;color:#fff;letter-spacing:.3px">SECTION <b style="color:var(--green)">BREAK</b></span>
    </div>
  </section>

  <section class="slide" style="left:621px;top:2352px" aria-label="Text and image slide">
    <div class="abs" style="left:0;top:0;width:290px;height:266px;background:var(--teal)"></div>
    <div class="brand-sm">Brunnfeld</div>
    <h2 class="title title--light" style="left:45px;top:36px">Lorem <span class="pill">ipsum</span><br>dolor sit amet</h2>
    <p class="body body--light abs" style="left:45px;top:140px;width:170px">Lorem ipsum dolor sit amet, consectetuer adipiscing elit, sed diam nonummy nibh euismod tincidunt ut laoreet dolore magna aliquam erat volutpat. Ut wisi enim ad minim veniam, quis nostrud exerci tation ullamcorper suscipit lobortis nisl ut aliquip ex ea commodo consequat. Duis autem vel eum iriure dolor in hendrerit in vulputate velit esse molestie consequat, vel illum dolore eu feugiat nulla facilisis at vero eros et accumsan et iusto.</p>
    <div class="bracket" style="left:225px;top:90px;width:230px;height:150px;border-top:none;border-left:none"></div>
    <div class="photo" role="img" aria-label="Photo of a doctor consulting an older patient" style="left:232px;top:80px;width:220px;height:150px;border-radius:8px;background:linear-gradient(135deg,#eceeec,#c6cec9)"></div>
    <div class="foot" style="color:#7fa09b">Your presentation title goes here | Brunnfeld GmbH 2023</div>
    <div class="pg">4</div>
  </section>

  <!-- Row 7 -->
  <section class="slide" style="left:122px;top:2649px" aria-label="Slide with two images">
    <div class="brand-sm">Brunnfeld</div>
    <h2 class="title" style="left:32px;top:40px">Slide <span class="pill">with</span><br>two images</h2>
    <div class="bracket" style="left:162px;top:64px;width:120px;height:95px;border-left:none;border-bottom:none"></div>
    <div class="photo" role="img" aria-label="Photo of an older man at home" style="left:165px;top:68px;width:115px;height:92px;border-radius:6px;background:linear-gradient(135deg,#d9cdbf,#a58c74)"></div>
    <p class="body abs" style="left:165px;top:170px;width:120px">Lorem ipsum dolor sit amet, consectetuer adipiscing elit, sed diam nonummy nibh euismod tincidunt ut laoreet dolore magna aliquam erat volutpat. Ut wisi enim ad minim veniam, quis nostrud exerci tation ullamcorper suscipit.</p>
    <div class="bracket" style="left:302px;top:64px;width:120px;height:95px;border-left:none;border-bottom:none"></div>
    <div class="photo" role="img" aria-label="Photo of a bright bedroom interior" style="left:305px;top:68px;width:115px;height:92px;border-radius:6px;background:linear-gradient(135deg,#e6ddd2,#b89c86)"></div>
    <p class="body abs" style="left:305px;top:170px;width:120px">Lorem ipsum dolor sit amet, consectetuer adipiscing elit, sed diam nonummy nibh euismod tincidunt ut laoreet dolore magna aliquam erat volutpat. Ut wisi enim ad minim veniam, quis nostrud exerci tation ullamcorper suscipit.</p>
    <div class="foot">Your presentation title goes here | Brunnfeld GmbH 2023</div>
    <div class="pg">4</div>
  </section>

</div>
</body>
</html>
```